Speisekarten-Design für gehobenes italienisches Restaurant
Zielgruppe
Wir sind ein gehobenes italienisches Restaurant und suchen ein neues Design für unsere Speisekarte. Wir haben ein eher älteres Publikum.
Aufgabenstellung
Wir möchten eine elegantes modernes Design. Einzelseiten im A4 Format.

```html
<!DOCTYPE html>
<html lang="de">
<head>
<meta charset="utf-8">
<title>Pasta – Nudelgerichte</title>
<link href="https://fonts.googleapis.com/css2?family=Mrs+Saint+Delafield&family=Libre+Baskerville:wght@400;700&family=Open+Sans:wght@400;600;700&display=swap" rel="stylesheet">
<style>
  :root {
    --wine: #7a1128;
    --ink: #333333;
    --text: #555555;
    --muted: #b5b5b5;
    --paper: #ffffff;
    --sketch-dark: #8a8a8a;
    --sketch-light: #e4e4e4;
    --cream: #f3e6b0;
  }
  * { margin: 0; padding: 0; box-sizing: border-box; }
  html, body { width: 848px; height: 1200px; overflow: hidden; background: var(--paper); }
  .menu-page {
    position: relative; width: 848px; height: 1200px; overflow: hidden;
    background: var(--paper); font-family: "Open Sans", sans-serif; color: var(--text);
  }
  .page-title {
    position: absolute; left: 0; right: 0; top: 30px; text-align: center;
    font-family: "Mrs Saint Delafield", cursive; font-weight: 400;
    font-size: 120px; line-height: 1; color: var(--wine); padding-left: 14px;
  }
  .page-subtitle {
    position: absolute; left: 0; right: 0; top: 152px; text-align: center;
    font-family: "Libre Baskerville", serif; font-weight: 700;
    font-size: 22px; letter-spacing: 1px; color: #111;
  }
  .column-divider {
    position: absolute; left: 422px; top: 226px; width: 1.5px; height: 440px; background: var(--wine);
  }
  .section-title {
    position: absolute; top: 250px; width: 360px; text-align: center;
    font-family: "Libre Baskerville", serif; font-weight: 400; font-size: 22px;
    letter-spacing: 1px; color: #111;
  }
  .section-title--forno { left: 46px; }
  .section-title--fresca { left: 453px; }
  .dish { position: absolute; }
  .col-left { left: 57px; }
  .col-right { left: 455px; }
  .dish-name {
    font-weight: 700; font-size: 14.5px; letter-spacing: 2.2px; line-height: 19px;
    color: var(--ink); white-space: nowrap;
  }
  .allergens {
    font-weight: 400; font-size: 8px; letter-spacing: 0.3px; color: var(--muted);
    vertical-align: 7px; margin-left: 2px;
  }
  .sep { font-weight: 400; font-size: 13px; color: var(--muted); letter-spacing: 0; margin: 0 14px 0 18px; }
  .price { font-size: 12px; letter-spacing: 0; color: var(--wine); }
  .dish-desc { font-size: 10.8px; line-height: 12.9px; color: var(--text); margin-top: 2px; }
  .plate-artwork { position: absolute; left: 0; top: 770px; width: 848px; height: 390px; }
  .footer-band {
    position: absolute; left: 0; bottom: 0; width: 848px; height: 41px; background: var(--wine);
    display: flex; align-items: center; justify-content: center; gap: 8px;
  }
  .brand-dot { width: 9px; height: 9px; border-radius: 50%; background: var(--cream); }
  .brand-name {
    font-family: "Open Sans", sans-serif; font-weight: 600; font-size: 17px;
    letter-spacing: 1px; color: var(--cream);
  }
</style>
</head>
<body>
<main class="menu-page">
  <h1 class="page-title">Pasta</h1>
  <p class="page-subtitle">NUDELGERICHTE</p>

  <div class="column-divider"></div>

  <h2 class="section-title section-title--forno">PASTA AL FORNO</h2>
  <h2 class="section-title section-title--fresca">PASTA FRESCA</h2>

  <article class="dish col-left" style="top:302px">
    <h3 class="dish-name">PENNE AL FORNO<span class="allergens">2,3,15,G,L,AH</span><span class="sep">//</span><span class="price">13,50 €</span></h3>
    <p class="dish-desc">Mit Schinken und Pilzen zubereitet und<br>mit einer Bolognese-Sahne-Soße überbacken</p>
  </article>

  <article class="dish col-left" style="top:370px">
    <h3 class="dish-name">LASAGNE<span class="allergens">G,AH</span><span class="sep">//</span><span class="price">13,50 €</span></h3>
    <p class="dish-desc">Der absolute Klassiker: Die italienische Schichtnudel-Spezialität</p>
  </article>

  <article class="dish col-left" style="top:425px">
    <h3 class="dish-name">TORTELLINI AL FORNO<span class="allergens">2,3,15,G,L,AH</span><span class="sep">//</span><span class="price">13,50 €</span></h3>
    <p class="dish-desc">Auch hier zubereitet mit Schinken<br>sowie Champignons. Und selbstverständlich<br>mit leckerer Bolognese-Sahne-Soße überbacken</p>
  </article>

  <article class="dish col-left" style="top:506px">
    <h3 class="dish-name">COMBINAZIONE<span class="allergens">AH,C,G,L</span><span class="sep">//</span><span class="price">14,90 €</span></h3>
    <p class="dish-desc">Freuen Sie sich auf verschiedene<br>Nudelspezialitäten, überbacken mit Bolognese-Soße</p>
  </article>

  <article class="dish col-right" style="top:303px">
    <h3 class="dish-name">TORTELLONI<br>GORGONZOLA<span class="allergens">G,AH,AW</span><span class="sep">//</span><span class="price">16,50 €</span></h3>
    <p class="dish-desc">Würzige Gorgonzolasoße gibt’s zu den<br>mit Ricotta-Käse und Spinat gefüllten Tortelloni</p>
  </article>

  <article class="dish col-right" style="top:390px">
    <h3 class="dish-name">TORTELLONI SPIRITO<span class="allergens">G,AH,AW</span><span class="sep">//</span><span class="price">15,90 €</span></h3>
    <p class="dish-desc">Die Tortelloni sind gefüllt mit Ricotta-Käse und Spinat,<br>zubereitet mit Zucchini, Erbsen und Champignons<br>erreicht Sie Ihr leckeres Nudelgericht mit Tomaten-Sahne-Soße</p>
  </article>

  <article class="dish col-right" style="top:470px">
    <h3 class="dish-name">TORTELLONI<br>‚STEINPILZE‘<span class="allergens">AH,AW,C,G,L</span><span class="sep">//</span><span class="price">16,50 €</span></h3>
    <p class="dish-desc">Frische mit Ricotta-Käse und Spinat gefüllte Tortelloni erwarten<br>Sie hier mit Steinpilzen in fein abgeschmeckter Rahmsoße</p>
  </article>

  <article class="dish col-right" style="top:556px">
    <h3 class="dish-name">TORTELLONI<br>‚BUTTER-SALBEI‘<span class="allergens">AH,AW,C,G,L</span><span class="sep">//</span><span class="price">15,90 €</span></h3>
    <p class="dish-desc">Frische mit Ricotta-Käse und Spinat<br>gefüllte Tortelloni kommen hier in Butter-Salbei-Soße daher,<br>getoppt von frischem Rucola und gehobeltem Parmesankäse</p>
  </article>

  <svg class="plate-artwork" viewBox="0 0 848 390" role="img" aria-label="Gezeichnete Illustration eines Tellers mit Pasta, Fleischbällchen, Basilikumblättern und Tomatenscheiben">
    <defs>
      <radialGradient id="plateTone" cx="50%" cy="80%" r="75%">
        <stop offset="0%" stop-color="var(--sketch-dark)"/>
        <stop offset="100%" stop-color="var(--sketch-light)"/>
      </radialGradient>
    </defs>
    <path d="M16 390 A408 388 0 0 1 832 390 Z" fill="url(#plateTone)"/>
  </svg>

  <footer class="footer-band">
    <span class="brand-dot"></span>
    <span class="brand-name">Casa Vellano</span>
  </footer>
</main>
</body>
</html>
```